Tarn Business Card Design Project

We have an existing business card. We are looking to creat a new card for the store. I have attached a my own business so you have a refference of what the current card looks like.

Phone: 1300 571 342
email: kelwood@tarnglazing.com.au
website: www.tarnglazing.com.au
Address: (Inside Kelwood Flooring Yard) 214 Farrow Rd, Marlow Park VIC 3172
Updates

This is a new business card for our store.

Industry/Entity Type

Business

Requirements
Must have
• Must look similar to the existing card

```html
<!DOCTYPE html>
<html lang="en">
<head>
<meta charset="utf-8">
<title>Tarn Shutters &amp; Blinds – Business Card</title>
<link rel="stylesheet" href="https://fonts.googleapis.com/css2?family=Arimo:wght@700&family=Michroma&display=swap">
<style>
  :root {
    --canvas: #5b6266;
    --card: #ecebe3;
    --tab: #ffffff;
    --ink: #161616;
    --slate: #4a4f52;
    --steel: #8a9398;
    --mist: #a9b0b3;
    --text: #3b3f42;
  }
  * { box-sizing: border-box; margin: 0; padding: 0; }
  html, body {
    width: 1200px; height: 900px; overflow: hidden;
    background: var(--canvas);
  }
  .canvas { position: relative; width: 1200px; height: 900px; }
  .card {
    position: absolute; left: 280px; width: 640px; height: 366px;
    background: var(--card);
    box-shadow: 0 8px 24px rgba(0,0,0,.35);
    overflow: hidden;
  }
  .card--front { top: 60px; }
  .card--back { top: 474px; }

  .motif {
    position: absolute;
    background: linear-gradient(135deg, var(--slate) 0%, var(--ink) 55%, var(--mist) 100%);
  }
  .card--front .motif { left: 36px; top: 40px; width: 290px; height: 220px; }
  .card--back .motif { left: 30px; top: 30px; width: 170px; height: 124px; }

  .brand { position: absolute; font-family: "Arimo", Arial, sans-serif; font-weight: 700; }
  .brand__name { display: block; color: var(--ink); letter-spacing: 1px; line-height: 1; }
  .brand__tagline { display: block; color: var(--steel); }

  .card--front .brand { left: 342px; top: 18px; }
  .card--front .brand__name { font-size: 76px; }
  .card--front .brand__tagline { font-size: 25px; margin-top: 6px; }

  .front__url {
    position: absolute; left: 320px; top: 318px;
    font-family: "Arimo", Arial, sans-serif; font-weight: 700;
    font-size: 19px; color: var(--text); letter-spacing: .3px;
  }

  .tab {
    position: absolute; right: 0; top: 0; width: 330px; height: 148px;
    background: var(--tab); border-bottom-left-radius: 28px;
  }
  .card--back .brand { left: 346px; top: 20px; }
  .card--back .brand__name { font-size: 64px; }
  .card--back .brand__tagline { font-size: 20px; margin-top: 6px; }

  .contact {
    position: absolute; left: 28px; top: 184px; list-style: none;
    font-family: "Michroma", sans-serif; font-size: 12px;
    color: var(--text); letter-spacing: 1.5px; text-transform: uppercase;
  }
  .contact__item { display: flex; align-items: flex-start; gap: 14px; margin-bottom: 10px; }
  .contact__item:last-child { margin-bottom: 0; }
  .contact__icon { width: 20px; height: 20px; flex: none; }
  .contact__lines { line-height: 20px; }
</style>
</head>
<body>
<main class="canvas">

  <section class="card card--front" aria-label="Card front">
    <div class="motif" role="img" aria-label="Cluster of overlapping grey, black and white squares"></div>
    <div class="brand">
      <span class="brand__name">Tarn</span>
      <span class="brand__tagline">Shutters &amp; Blinds</span>
    </div>
    <p class="front__url">www.tarnglazing.com.au</p>
  </section>

  <section class="card card--back" aria-label="Card back">
    <div class="tab"></div>
    <div class="brand">
      <span class="brand__name">Tarn</span>
      <span class="brand__tagline">Shutters &amp; Blinds</span>
    </div>
    <div class="motif" role="img" aria-label="Small cluster of overlapping grey, black and white squares"></div>

    <ul class="contact">
      <li class="contact__item">
        <svg class="contact__icon" viewBox="0 0 24 24" aria-hidden="true"><path d="M6 3l3 4-2 2c1 3 4 6 7 7l2-2 4 3-2 3C10 20 4 14 3 5z" fill="none" stroke="#161616" stroke-width="1.6" stroke-linejoin="round"/></svg>
        <span class="contact__lines">1300 571 342</span>
      </li>
      <li class="contact__item">
        <svg class="contact__icon" viewBox="0 0 24 24" aria-hidden="true"><path d="M12 2a7 7 0 0 0-7 7c0 5 7 13 7 13s7-8 7-13a7 7 0 0 0-7-7z" fill="#161616"/><circle cx="12" cy="9" r="2.6" fill="#ecebe3"/></svg>
        <span class="contact__lines">(Inside Kelwood Flooring Yard)<br>214 Farrow Rd, Marlow Park VIC 3172</span>
      </li>
      <li class="contact__item">
        <svg class="contact__icon" viewBox="0 0 24 24" aria-hidden="true"><g fill="none" stroke="#161616" stroke-width="1.5"><circle cx="12" cy="12" r="9.5"/><ellipse cx="12" cy="12" rx="4.5" ry="9.5"/><path d="M2.5 12h19M4 7h16M4 17h16"/></g></svg>
        <span class="contact__lines">www.tarnglazing.com.au</span>
      </li>
      <li class="contact__item">
        <svg class="contact__icon" viewBox="0 0 24 24" aria-hidden="true"><g fill="none" stroke="#161616" stroke-width="1.5"><rect x="2" y="5" width="20" height="14"/><path d="M2 5l10 8 10-8M2 19l7-7M22 19l-7-7"/></g></svg>
        <span class="contact__lines">kelwood@tarnglazing.com.au</span>
      </li>
    </ul>
  </section>

</main>
</body>
</html>
```